Business Card Design Project

We need a business card design for a new boutique consulting company, TivaConsulting. Our new logo has just been designed and we are looking for simple, clean looking business cards. Logo attached

Industry/Entity Type

Boutique

Requirements
Must have
• There must be room for each card to have the following details:
Name
Title
Address - 2 lines
Phone number
Email address
Website address

Nice to have
• May have something on the back of the buisness card - emphasing the word "Tiva".

```html
<!DOCTYPE html>
<html lang="en">
<head>
<meta charset="utf-8">
<title>TivaConsulting Business Card</title>
<link href="https://fonts.googleapis.com/css2?family=Open+Sans:wght@400;600&display=swap" rel="stylesheet">
<style>
  :root {
    --page: #ffffff;
    --green: #7dbb33;
    --band-green: #8cc63f;
    --header-beige: #e6e2d9;
    --card-pale: #f3f1ec;
    --back-edge: #d6cfb4;
    --white: #ffffff;
  }
  html, body {
    margin: 0;
    padding: 0;
    overflow: hidden;
    background: var(--page);
  }
  .canvas {
    position: relative;
    width: 1200px;
    height: 900px;
    overflow: hidden;
    background: var(--page);
    font-family: "Open Sans", Arial, sans-serif;
  }
  .card-front {
    position: absolute;
    left: 264px;
    top: 36px;
    width: 668px;
    height: 384px;
    background: linear-gradient(to bottom, var(--white) 0%, var(--white) 45%, var(--card-pale) 100%);
  }
  .front-header {
    position: absolute;
    left: 0;
    top: 0;
    width: 100%;
    height: 74px;
    background: var(--header-beige);
  }
  .brand {
    display: flex;
    align-items: center;
    gap: 10px;
    color: var(--green);
    font-weight: 600;
    letter-spacing: -0.5px;
    white-space: nowrap;
  }
  .brand-mark {
    background: var(--green);
    flex: none;
  }
  .front-header .brand {
    position: absolute;
    right: 12px;
    top: 10px;
    font-size: 42px;
    line-height: 54px;
  }
  .front-header .brand-mark {
    width: 18px;
    height: 18px;
  }
  .employee {
    position: absolute;
    left: 76px;
    top: 110px;
    width: 216px;
    text-align: right;
    color: var(--green);
  }
  .employee-name {
    margin: 0;
    font-size: 30px;
    line-height: 40px;
    font-weight: 400;
  }
  .employee-title {
    margin: 0;
    font-size: 26px;
    line-height: 40px;
    font-weight: 400;
  }
  .address {
    position: absolute;
    left: 418px;
    top: 112px;
    margin: 0;
    font-style: normal;
    color: var(--green);
    font-size: 21px;
    line-height: 30px;
  }
  .address .phone {
    font-weight: 600;
  }
  .contact-band {
    position: absolute;
    left: 0;
    bottom: 0;
    width: 100%;
    height: 76px;
    background: var(--band-green);
    color: var(--white);
    text-align: center;
    font-size: 21px;
    line-height: 28px;
    padding-top: 10px;
    box-sizing: border-box;
  }
  .card-back {
    position: absolute;
    left: 262px;
    top: 456px;
    width: 670px;
    height: 384px;
    background: radial-gradient(ellipse 420px 260px at 32% 50%, var(--white) 0%, #ece8da 45%, var(--back-edge) 100%);
    display: flex;
    align-items: center;
    justify-content: center;
  }
  .card-back .brand {
    font-size: 72px;
    line-height: 90px;
    gap: 16px;
  }
  .card-back .brand-mark {
    width: 30px;
    height: 30px;
  }
</style>
</head>
<body>
<div class="canvas">
  <section class="card-front" aria-label="Business card front">
    <header class="front-header">
      <div class="brand"><span class="brand-mark"></span><span class="brand-name">TivaConsulting</span></div>
    </header>
    <div class="employee">
      <p class="employee-name">employee name</p>
      <p class="employee-title">job title</p>
    </div>
    <address class="address">
      Address 1<br>
      Address 2<br>
      <span class="phone">Phone: (07) 5550 1284</span>
    </address>
    <div class="contact-band">
      email: sales@tivaconsulting.com<br>
      web: www.tivaconsulting.com
    </div>
  </section>

  <section class="card-back" aria-label="Business card back">
    <div class="brand"><span class="brand-mark"></span><span class="brand-name">TivaConsulting</span></div>
  </section>
</div>
</body>
</html>
```